Give my personal webpage more appeal!

I need my CV website improved - drmeganholt.com.au.
I am using the template KESTREL from pagecraftly. i would like to keep the already existing theme but am open to suggestions.
Please focus on imagery, colour scheme, and textures to enhance the appeal and look of the page.
The content is there, but now I need a designer to improve the look of my page.
I need styling, royalty-free unique modern images to make the page professional, personal and friendly.
I work in healthcare, so I'm a people person.
I teach professionals and I treat a lot of families.

Target Market(s)

Parents, Professional Healthcare providers

Number of Pages Required

1 page

Font styles to use
Serif
Sans Serif

Requirements
Must have
• My face - image at the top, all the information already contained in it.
• Links to the websites I manage such as my blog.
• One Page website.
• All the information it already contains with the ability to have more.
• Ideally, we would keep the same format for the page although I'm happy to expand column and change the page's structure with in the theme template KESTREL.
Nice to have
• The current KESTREL template. I would like to keep the already existing theme but am open to suggestions.
Should not have
• Multiple pages.

```html
<!DOCTYPE html>
<html lang="en">
<head>
<meta charset="utf-8">
<title>Dr Megan Holt – CV</title>
<link href="https://fonts.googleapis.com/css2?family=Montserrat:wght@400;600;700;800&family=Roboto:wght@400;500&display=swap" rel="stylesheet">
<style>
  :root{
    --coral:#f04e5f;
    --ink:#141414;
    --body:#5d5d5d;
    --muted:#8c8c8c;
    --panel:#f6f6f6;
    --white:#ffffff;
    --logo:#9b9b9b;
  }
  *{margin:0;padding:0;box-sizing:border-box}
  html,body{width:1200px;height:1000px;overflow:hidden;background:var(--white)}
  body{position:relative;font-family:'Roboto',Arial,sans-serif}

  .education-band{position:absolute;left:184px;top:0;width:1016px;height:136px;background:var(--coral)}
  .edu-item{position:absolute;color:var(--white);font-family:'Montserrat',Arial,sans-serif;font-size:11.5px;letter-spacing:.4px;line-height:15px;white-space:nowrap}
  .edu-item .ring{position:absolute;left:-62px;top:-36px;width:44px;height:44px;border:2px solid var(--white);border-radius:50%}
  .edu-brisbane{left:432px;top:-8px}
  .edu-sydney{left:792px;top:-11px}

  .employment{position:absolute;left:184px;top:136px;width:1016px;height:455px;background:var(--panel)}
  .employment-rule{position:absolute;left:184px;top:591px;width:1016px;height:8px;background:var(--coral)}
  .section-title{position:absolute;left:346px;top:213px;font-family:'Montserrat',Arial,sans-serif;font-weight:800;font-size:17px;color:var(--ink);letter-spacing:.2px}
  .section-title::before{content:"";position:absolute;left:-18px;top:11px;width:8px;height:2px;background:var(--coral)}

  .job{position:absolute;top:264px;width:172px}
  .job h3{font-family:'Montserrat',Arial,sans-serif;font-weight:700;font-size:8.4px;color:var(--ink);line-height:14.5px;text-transform:uppercase}
  .job .role{font-family:'Montserrat',Arial,sans-serif;font-weight:600;font-size:8.4px;color:var(--muted);line-height:14.5px;text-transform:uppercase}
  .job .dates{position:relative;margin:4px 0 9px;height:16px}
  .job .dates span{position:absolute;left:0;top:0;background:var(--ink);color:var(--white);font-family:'Montserrat',Arial,sans-serif;font-weight:700;font-size:7.6px;padding:0 8px;line-height:16px}
  .job .dates::after{content:"";position:absolute;left:0;right:0;top:8px;height:1px;background:var(--ink);z-index:-1}
  .job .dates.short::after{right:70px}
  .job p{font-size:8.3px;line-height:14.5px;color:var(--body);margin-bottom:6px;width:164px}
  .job-1{left:346px}
  .job-2{left:531px}
  .job-3{left:715px}
  .job-4{left:899px}

  .sites-title{position:absolute;left:0;width:1388px;top:648px;text-align:center;font-family:'Montserrat',Arial,sans-serif;font-weight:800;font-size:18.5px;color:#2b2b2b;letter-spacing:.3px}
  .site-link{position:absolute;display:flex;align-items:center;justify-content:center;gap:8px;color:var(--logo);font-family:'Montserrat',Arial,sans-serif;font-weight:600;text-decoration:none;white-space:nowrap;text-align:center}
  .site-link .dot{width:14px;height:14px;border-radius:50%;background:var(--logo)}
  .site-blog{left:320px;top:755px;width:176px;font-size:21px}
  .site-gut{left:562px;top:752px;width:180px;font-size:25px}
  .site-reflex{left:790px;top:724px;width:120px;flex-direction:column;gap:10px;font-size:16px}
  .site-reflex .dot{width:40px;height:40px}
  .site-learn{left:940px;top:760px;width:150px;font-size:13.5px}

  .social-band{position:absolute;left:182px;top:925px;width:1018px;height:64px;background:var(--coral)}
  .social-title{position:absolute;left:291px;top:946px;font-family:'Montserrat',Arial,sans-serif;font-weight:700;font-size:18px;color:var(--white);letter-spacing:.4px;white-space:nowrap}
  .social-link{position:absolute;top:939px;height:37px;display:flex;align-items:center;gap:8px;color:var(--white);font-family:'Montserrat',Arial,sans-serif;font-weight:700;font-size:13px;text-decoration:none;white-space:nowrap}
  .social-link .disc{width:22px;height:22px;border-radius:50%;background:var(--white)}
  .social-a{left:621px}
  .social-b{left:735px}
</style>
</head>
<body>
  <section class="education-band"></section>
  <div class="edu-item edu-brisbane"><span class="ring"></span>Bachelor of Science (Anatomy),<br>BRISBANE, AUSTRALIA 1997-1999</div>
  <div class="edu-item edu-sydney"><span class="ring"></span>Master of Chiropractic,<br>SYDNEY, AUSTRALIA 2000-2002</div>

  <section class="employment"></section>
  <h2 class="section-title">EMPLOYMENT</h2>

  <article class="job job-1">
    <h3>Bright Spine Studio</h3>
    <div class="role">Founder, Chiropractor</div>
    <div class="dates"><span>2005-2017</span></div>
    <p>What a wonderful place to work! I can't come to this clinic and not feel happy. It's decorated for the hundreds of children who get treated here. I've been privileged to watch so many families blossoms through the stages of infancy to teens. They feel like family.</p>
    <p>My job here as Chiropractor has been to train my Chiropractic Associates, Chiropractic Assistants and support staff. To keep the standards high, the team managed and motivated, and the clinic excelling.  In July 2016 I sold this business but I continue to work here as an Associate Chiropractor.</p>
  </article>

  <article class="job job-2">
    <h3>Harbourside Spine &amp; Health Centre</h3>
    <div class="role">Associate Chiropractor</div>
    <div class="dates"><span>2004-2005</span></div>
    <p>I learned a lot from my mentor Dr Owen Farley here.  He taught me how to think like a business woman, which was exactly what I needed for my next move.</p>
  </article>

  <article class="job job-3">
    <h3>Kindred Wellness Centre</h3>
    <div class="role">Associate Chiropractor</div>
    <div class="dates"><span>2003-2004</span></div>
    <p>Working under Dr Lionel Marsh has been the greatest gift I could have imagined first year out of University.  He taught me his life's learnings and I have treasured them. He taught me that the greatest gift for any teacher is to have their student surpass them.  He taught me how to be an ego free teacher, share my knowledge unreservedly with those who ask, and how to life without expectations. He shaped me into the practitioner and teacher I have become.</p>
  </article>

  <article class="job job-4">
    <h3>Eastgate University</h3>
    <div class="role">Chiropractic Skills Tutor and Examiner</div>
    <div class="dates short"><span>2002</span></div>
    <p>What an honour to be invited to tutor and examine 2nd year Chiropractic Skills whilst in my final year of my Masters of Chiropractic.  And what a delightful bunch of students we had that year too!</p>
  </article>

  <div class="employment-rule"></div>

  <h2 class="sites-title">VISIT MY WEBSITES</h2>
  <a class="site-link site-blog" href="#">dr Megans blog</a>
  <a class="site-link site-gut" href="#">GutWise OZ</a>
  <a class="site-link site-reflex" href="#"><span class="dot"></span>Reflex Roots</a>
  <a class="site-link site-learn" href="#">learnkinesio.com.au</a>

  <footer class="social-band"></footer>
  <div class="social-title">FIND ME ON SOCIAL MEDIA</div>
  <a class="social-link social-a" href="#"><span class="disc"></span>Friendsly</a>
  <a class="social-link social-b" href="#"><span class="disc"></span>Linkwork</a>
</body>
</html>
```